Brightvale services brochure

We need a new company brochure. The brochure will be formatted for PDF distribution but should be printable on "letter" size paper. 2 pages plus front and back cover. Color white and same blue as logo. Logo "O" should be used as design. Look at webpage for general info: www.brightvale-example.ca<br/><br/>Front cover: pic1, logo, design and "Your Cleaning is Our Business". <br/>Back cover" "O" design, logo and info from "contact" page<br/>Front cover inside: design and intro from web home page, also use stock pics of clean offices ect as placeholders for purchased pics.<br/>1st page: design and "Our Services", use info of "Cleanroom & GMP Services", "Janitorial Services" from services page.<br/>2nd page: design and "Special Services", info from "Carpet & Upholstery Services", "Window Cleaning Services", and list of "Other Services".<br/>Back cover inside : design and info from technology page, use stock pics for place holders.

Industry/Entity Type

Janitorial

Font styles to use
Sans Serif
Other font styles liked:
• Futura Book

Colors
0555a3

Requirements
Must have
• The logo "O" (target) should be part of the design. Design color same as logo.

```html
<!DOCTYPE html>
<html lang="en">
<head>
<meta charset="utf-8">
<title>Brightvale – Special Services</title>
<link href="https://fonts.googleapis.com/css2?family=Titillium+Web:wght@300;400&display=swap" rel="stylesheet">
<style>
  :root {
    --brand-blue: #1a80c4;
    --brand-blue-soft: #d7e9f6;
    --text-grey: #474747;
    --heading-grey: #5a5a5a;
    --paper: #ffffff;
  }
  html, body {
    margin: 0;
    padding: 0;
    overflow: hidden;
    background: var(--paper);
  }
  .page {
    position: relative;
    width: 927px;
    height: 1200px;
    overflow: hidden;
    background: var(--paper);
    font-family: "Titillium Web", "Trebuchet MS", sans-serif;
    color: var(--text-grey);
  }
  .section-band {
    position: absolute;
    left: 188px;
    width: 652px;
    height: 63px;
  }
  .section-band svg { position: absolute; inset: 0; }
  .section-band h2 {
    position: absolute;
    left: 28px;
    top: 8px;
    margin: 0;
    font-weight: 400;
    font-size: 31px;
    letter-spacing: 0.3px;
    color: var(--paper);
    line-height: 1;
  }
  .band-special { top: 53px; }
  .band-other { top: 774px; }

  .service-icon {
    position: absolute;
    left: 56px;
    width: 108px;
    height: 108px;
  }
  .icon-carpet { top: 132px; }
  .icon-window { top: 580px; }

  .service {
    position: absolute;
    left: 188px;
    width: 660px;
  }
  .service h3 {
    margin: 0 0 2px;
    font-weight: 300;
    font-size: 20.5px;
    line-height: 26px;
    color: var(--heading-grey);
  }
  .service p {
    margin: 0;
    font-weight: 300;
    font-size: 15.6px;
    line-height: 24.05px;
    white-space: nowrap;
  }
  .service-carpet { top: 135px; }
  .service-window { top: 575px; }

  .other-list {
    position: absolute;
    left: 538px;
    top: 867px;
    margin: 0;
    font-weight: 300;
    font-size: 16.2px;
    line-height: 24.05px;
    white-space: nowrap;
  }
  .photo-frame {
    position: absolute;
    left: -20px;
    top: 848px;
    width: 452px;
    height: 452px;
  }
  .corner-disc {
    position: absolute;
    left: 400px;
    top: 1124px;
    width: 340px;
    height: 200px;
  }
</style>
</head>
<body>
<main class="page">

  <header class="section-band band-special">
    <svg width="652" height="63" viewBox="0 0 652 63" aria-hidden="true">
      <path d="M20 0 H252 C262 0 266 6 272 12 L280 20 C285 25 290 26 300 26 H630 A18.5 18.5 0 0 1 630 63 H20 A20 20 0 0 1 0 43 V20 A20 20 0 0 1 20 0 Z" fill="var(--brand-blue)"/>
    </svg>
    <h2>Special Services</h2>
  </header>

  <svg class="service-icon icon-carpet" viewBox="0 0 108 108" role="img" aria-label="Icon of a person vacuuming carpet">
    <circle cx="54" cy="54" r="52.5" fill="none" stroke="var(--brand-blue)" stroke-width="1.6"/>
    <circle cx="54" cy="54" r="30" fill="var(--brand-blue-soft)"/>
  </svg>

  <section class="service service-carpet">
    <h3>Carpet &amp; Upholstery Services</h3>
    <p>Office furnishings such as carpets, drapes and upholstered furniture represent a serious<br>
investment to a company. We maintain this investment with care and quality that extends<br>
the lifespan of furniture and carpet. Where many of our competitors offer a narrow range of<br>
cleaning and maintenance options, Brightvale utilizes specialized equipment at any given<br>
location. This means that your furnishings will be handled appropriately, taking into<br>
consideration the varying soiling conditions, type of carpeting or fabric, in addition to<br>
responding to weight, color, backing, underlay and texture. In other words, you get the<br>
cleaning method that’s best for you! In high traffic areas Rotary Shampooing techniques<br>
remove stubborn stains. Steam Cleaning and Hot Water Extraction techniques clean and<br>
flush grit and residue to thoroughly clean carpets deep into their core. Bonnet Buff systems<br>
spray and massage carpets removing emulsified dirt. Pile Lifting, Dry Cleaning and straight<br>
vacuuming is also used where appropriate and effective. Care of upholstered furniture is just<br>
as rigorous. We are able to service all materials and fabrics using shampoo, steam cleaning<br>
and dry cleaning techniques that are appropriate. To ensure the longevity of your carpet and<br>
upholstery, we use state of the art Fiber Protection Systems. Our objective is to provide you<br>
with the cleanest possible surfaces while at the same time assure the safest results.</p>
  </section>

  <svg class="service-icon icon-window" viewBox="0 0 108 108" role="img" aria-label="Icon of a person cleaning a window">
    <circle cx="54" cy="54" r="52.5" fill="none" stroke="var(--brand-blue)" stroke-width="1.6"/>
    <circle cx="54" cy="54" r="30" fill="var(--brand-blue-soft)"/>
  </svg>

  <section class="service service-window">
    <h3>Window Cleaning Services</h3>
    <p>We can implement a regular program of interior and exterior window cleaning, or we can<br>
meet your needs as a project basis. We have the staff and equipment to tackle both<br>
high-rise and low level window cleaning. In addition to windows, we are also prepared to<br>
handle all your awning and canopy sign cleaning needs, as well as lighting element<br>
replacement when required. Brightvale has built its impressive customer list by satisfying<br>
every challenge building management has passed our way.</p>
  </section>

  <header class="section-band band-other">
    <svg width="652" height="63" viewBox="0 0 652 63" aria-hidden="true">
      <path d="M20 0 H252 C262 0 266 6 272 12 L280 20 C285 25 290 26 300 26 H630 A18.5 18.5 0 0 1 630 63 H20 A20 20 0 0 1 0 43 V20 A20 20 0 0 1 20 0 Z" fill="var(--brand-blue)"/>
    </svg>
    <h2>Other Services</h2>
  </header>

  <svg class="photo-frame" viewBox="0 0 452 452" role="img" aria-label="Photo of a cleaner vacuuming a light carpet in a bright living room">
    <defs>
      <radialGradient id="photoTone" cx="50%" cy="45%" r="60%">
        <stop offset="0" stop-color="#e9e6e2"/>
        <stop offset="0.6" stop-color="#d6d0c9"/>
        <stop offset="1" stop-color="#b9b1a8"/>
      </radialGradient>
    </defs>
    <circle cx="226" cy="226" r="214" fill="url(#photoTone)"/>
    <circle cx="226" cy="226" r="214" fill="none" stroke="var(--brand-blue)" stroke-width="9"/>
  </svg>

  <p class="other-list">Day Porter Services &nbsp;| &nbsp;Construction<br>
Clean-Ups &nbsp;| &nbsp;Quality Control Inspections<br>
Maid Services &nbsp;| &nbsp;Light &amp; Ceiling Fixture<br>
Cleaning &nbsp;| &nbsp;Wall Washing Drapery &amp; Blind<br>
Cleaning &nbsp;| &nbsp;Acoustical Tile Cleaning<br>
Computer Terminal, Monitor and Keyboard<br>
Cleaning &nbsp;| &nbsp;Marble, Granite &amp; Terrazzo<br>
Refinishing &amp; Maintenance<br>
Power Washing</p>

  <svg class="corner-disc" viewBox="0 0 340 200" aria-hidden="true">
    <circle cx="170" cy="175" r="175" fill="var(--brand-blue)"/>
  </svg>

</main>
</body>
</html>
```